Trade show background graphics design

Our company is planning to participate a exhibit. we have 10X10 booth, and we want to set up a display in the background. this project is to get the best design for this background. It will be printed on a 10X8 or 8X8 vinyl fabrics. some relevant information:

our company website:
http://www.quorvantel.net/about-you

Exhibit information:
http://www.trelvixexpo.org/trelvix2017/public/enter.aspx

Target Market(s)

building owner, facility management company

Industry/Entity Type

It Company

Font styles to use
Serif

Colors

Designer to choose colors to be used in the design.

Requirements
Must have
• Company Logo
Nice to have
• Highlights or description of our services

```html
<!DOCTYPE html>
<html lang="en">
<head>
<meta charset="utf-8">
<title>Quorvantel – Trade Show Backdrop</title>
<link rel="stylesheet" href="https://fonts.googleapis.com/css2?family=Fjalla+One&family=Open+Sans:wght@700&display=swap">
<style>
  :root {
    --navy: #1a4f8c;
    --blue: #2470b0;
    --blue-light: #3a8cc8;
    --hex-fill: #1f86b0;
    --hex-edge: #cfdf3c;
    --accent-green: #b4d235;
    --bullet-yellow: #f6cf15;
    --white: #ffffff;
    --photo-a: #c9d3dc;
    --photo-b: #7d95ab;
  }
  * { margin: 0; padding: 0; box-sizing: border-box; }
  html, body { width: 1200px; height: 725px; overflow: hidden; background: #ffffff; }
  .backdrop {
    position: relative;
    width: 1200px;
    height: 725px;
    overflow: hidden;
    background:
      radial-gradient(ellipse 520px 260px at 600px 200px, rgba(90,160,215,0.35), transparent 70%),
      radial-gradient(ellipse 300px 200px at 200px 180px, rgba(90,160,215,0.25), transparent 70%),
      linear-gradient(180deg, var(--blue) 0%, var(--navy) 100%);
    font-family: "Open Sans", Arial, sans-serif;
    color: var(--white);
  }
  .world-map {
    position: absolute; left: 0; top: 30px; width: 1200px; height: 420px;
    background: radial-gradient(ellipse 560px 200px at 560px 210px, rgba(120,185,230,0.18), transparent 75%);
  }
  .skyline {
    position: absolute; left: 0; bottom: 0; width: 1200px; height: 330px;
    background: linear-gradient(180deg, rgba(30,80,140,0) 0%, rgba(28,74,130,0.55) 60%, rgba(26,68,122,0.7) 100%);
  }
  .graphics { position: absolute; left: 0; top: 0; }

  .brand { position: absolute; left: 62px; top: 70px; display: flex; align-items: center; gap: 14px; }
  .brand-mark { width: 30px; height: 30px; background: var(--accent-green); }
  .brand-name { font-family: "Fjalla One", sans-serif; font-size: 46px; letter-spacing: 3px; color: var(--accent-green); }
  .tagline {
    position: absolute; left: 72px; top: 171px;
    font-family: "Fjalla One", sans-serif; font-size: 21px; letter-spacing: 0.2px; color: var(--white);
  }

  .hex-label {
    position: absolute; width: 200px; text-align: center;
    font-family: "Fjalla One", sans-serif; font-size: 31px; line-height: 38px; color: var(--white);
  }
  .hex-label--results { left: 370px; top: 270px; }
  .hex-label--data { left: 540px; top: 376px; }
  .hex-label--turnkey { left: 370px; top: 452px; }

  .service-heading {
    position: absolute; right: 308px; text-align: right;
    font-family: "Fjalla One", sans-serif; font-size: 19px; line-height: 22.5px; color: var(--accent-green);
  }
  .service-point {
    position: absolute; left: 922px; width: 250px;
    font-size: 14.6px; line-height: 19.5px; font-weight: 700; color: var(--white);
  }
</style>
</head>
<body>
<main class="backdrop">
  <div class="world-map" role="img" aria-label="Faint world map in the background"></div>
  <div class="skyline" role="img" aria-label="Faint city skyline silhouette along the bottom"></div>

  <svg class="graphics" width="1200" height="725" viewBox="0 0 1200 725">
    <defs>
      <polygon id="mini-hex" points="-12,0 -6,-10.4 6,-10.4 12,0 6,10.4 -6,10.4"/>
      <polygon id="bullet-hex" points="-10,0 -5,-8.7 5,-8.7 10,0 5,8.7 -5,8.7"/>
      <linearGradient id="photo-office" x1="0" y1="0" x2="1" y2="1">
        <stop offset="0" stop-color="#eef1f4"/><stop offset="1" stop-color="#aab8c6"/>
      </linearGradient>
      <linearGradient id="photo-team" x1="0" y1="0" x2="1" y2="1">
        <stop offset="0" stop-color="#e6e3dc"/><stop offset="1" stop-color="#5d6f86"/>
      </linearGradient>
      <linearGradient id="photo-gears" x1="0" y1="0" x2="0" y2="1">
        <stop offset="0" stop-color="#5f6a66"/><stop offset="1" stop-color="#2c3236"/>
      </linearGradient>
    </defs>

    <!-- connector lines -->
    <g class="connectors" fill="none" stroke="var(--white)" stroke-width="1.6" stroke-dasharray="5 4">
      <polyline points="143,625 143,393 228,393"/>
      <polyline points="303,670 365,670 365,557 420,557"/>
      <polyline points="709,230 752,230 752,525 692,525"/>
    </g>

    <!-- image hexagons -->
    <g role="img" aria-label="Photo of a laptop with printed charts on a desk">
      <polygon points="538,190 589,102 691,102 742,190 691,278 589,278" fill="url(#photo-office)"/>
    </g>
    <g role="img" aria-label="Photo of engineers in hard hats reviewing plans">
      <polygon points="200,390 251,302 353,302 404,390 353,478 251,478" fill="url(#photo-team)"/>
    </g>
    <g role="img" aria-label="Photo of hands typing on a laptop under colourful gears">
      <polygon points="538,600 589,512 691,512 742,600 691,688 589,688" fill="url(#photo-gears)"/>
    </g>

    <!-- value hexagons -->
    <g class="value-hexes" fill="var(--hex-fill)" stroke="var(--hex-edge)" stroke-width="5">
      <polygon points="368,295 419,207 521,207 572,295 521,383 419,383"/>
      <polygon points="538,395 589,307 691,307 742,395 691,483 589,483"/>
      <polygon points="368,489 419,401 521,401 572,489 521,577 419,577"/>
    </g>

    <!-- small node hexagons -->
    <g class="nodes" fill="var(--white)">
      <use href="#mini-hex" x="432" y="364"/>
      <use href="#mini-hex" x="598" y="460"/>
      <use href="#mini-hex" x="432" y="557"/>
      <use href="#mini-hex" x="697" y="230"/>
      <use href="#mini-hex" x="680" y="525"/>
      <use href="#mini-hex" x="228" y="393"/>
      <use href="#mini-hex" x="143" y="625"/>
      <use href="#mini-hex" x="303" y="670"/>
    </g>

    <!-- services timeline -->
    <line x1="905" y1="100" x2="905" y2="612" stroke="var(--white)" stroke-width="2.5"/>
    <g class="bullets" fill="var(--bullet-yellow)">
      <use href="#bullet-hex" x="905" y="104"/>
      <use href="#bullet-hex" x="905" y="126"/>
      <use href="#bullet-hex" x="905" y="202"/>
      <use href="#bullet-hex" x="905" y="251"/>
      <use href="#bullet-hex" x="905" y="308"/>
      <use href="#bullet-hex" x="905" y="367"/>
      <use href="#bullet-hex" x="905" y="469"/>
      <use href="#bullet-hex" x="905" y="508"/>
      <use href="#bullet-hex" x="905" y="548"/>
      <use href="#bullet-hex" x="905" y="586"/>
    </g>
  </svg>

  <div class="brand">
    <span class="brand-mark"></span>
    <span class="brand-name">QUORVANTEL</span>
  </div>
  <p class="tagline">WE MAXIMIZE YOUR BUILDING EFFICIENCY</p>

  <p class="hex-label hex-label--results">EXCEPTIONAL<br>RESULTS</p>
  <p class="hex-label hex-label--data">DATA DRIVEN</p>
  <p class="hex-label hex-label--turnkey">TURNKEY<br>SOLUTION</p>

  <h2 class="service-heading" style="top:93px">COMMISSIONING<br>AND OPTIMIZATION</h2>
  <p class="service-point" style="top:94px">Systematic Approach</p>
  <p class="service-point" style="top:115px">Customized solution<br>tailored based on<br>each site<br>characteristics</p>
  <p class="service-point" style="top:192px">Turkey solution and<br>Saving Guarantee</p>

  <h2 class="service-heading" style="top:244px">MONITORING-<br>BASED<br>COMMISSIONING</h2>
  <p class="service-point" style="top:240px">Customized analytic rule<br>sets tailored based on each<br>site need</p>
  <p class="service-point" style="top:297px">Utilizing real-time data and<br>customized energy dash<br>board</p>
  <p class="service-point" style="top:356px">Built in work order flow<br>system and other features<br>to serve different needs of<br>customer</p>

  <h2 class="service-heading" style="top:462px">BUILDING<br>AUTOMATION<br>SYSTEM</h2>
  <p class="service-point" style="top:459px">30 years' experience in<br>building automation</p>
  <p class="service-point" style="top:498px">Third party service to<br>legacy control system</p>
  <p class="service-point" style="top:538px">Expert in system<br>integration</p>
  <p class="service-point" style="top:576px">Expert in providing<br>upgrade solution and<br>turn-key installation</p>
</main>
</body>
</html>
```